UI Design & Web Design for Used Car Dealer.
Modern and user friendly responsive layout for mobiles and desktop. Bootstrap and form elements for members,registration process,login,dashboard. Layouts for Home Page, Car Listing Pages, Individual Car Information page and etc.

Output files in Bootstrap Html/CSS
Please refer to attachments for more details.

Target Market(s)

Asia / Singapore

Industry/Entity Type

Car Dealer

Coding

Coded - Design and coding required

Number of Pages Required

5+ page

Font styles to use
Sans Serif

Colors
acd037
f6faec
cfcfcf
b1b1b1
ffffff

Requirements
Must have
• Coded in Bootstrap 3 UI Elements, Forms, Labels, Sections, Tables, Buttons, Alerts, Modal, Fonts, Dashboard, Login, Register,Contact
Nice to have
• Stock Images
Should not have
• NA

```html
<!DOCTYPE html>
<html lang="en">
<head>
<meta charset="utf-8">
<title>Drivemarq — Home</title>
<link href="https://fonts.googleapis.com/css2?family=Open+Sans:wght@400;600;700&display=swap" rel="stylesheet">
<style>
  :root {
    --brand-green: #acd037;
    --brand-tint: #f6faec;
    --grey-light: #cfcfcf;
    --grey-mid: #b1b1b1;
    --white: #ffffff;
    --nav-text: #333333;
    --footer-bg: #ebebeb;
    --footer-text: #6b6b6b;
    --body-muted: #c9c9c9;
    --button-bg: #9a9a9a;
    --button-text: #f2f2f2;
    --hero-top: #9a9893;
    --hero-mid: #5a5149;
    --hero-bottom: #0f0c0a;
  }
  * { box-sizing: border-box; margin: 0; padding: 0; }
  html, body { width: 1200px; height: 994px; overflow: hidden; }
  body { font-family: "Open Sans", Arial, sans-serif; background: var(--white); position: relative; }

  .top-strip { position: absolute; top: 0; left: 0; width: 1200px; height: 3px; background: var(--brand-green); }

  .site-header { position: absolute; top: 3px; left: 0; width: 1200px; height: 69px; background: var(--white); }
  .brand { position: absolute; left: 132px; top: 17px; display: flex; align-items: center; gap: 12px; }
  .brand-mark { width: 38px; height: 38px; background: var(--brand-green); border-radius: 3px; }
  .brand-name { font-size: 24px; font-weight: 700; color: var(--brand-green); letter-spacing: 1px; }
  .main-nav { position: absolute; right: 133px; top: 29px; display: flex; gap: 26px; font-size: 11.5px; }
  .main-nav a { color: var(--nav-text); text-decoration: none; text-transform: uppercase; }
  .main-nav a.is-active { color: var(--brand-green); }

  .hero { position: absolute; top: 72px; left: 0; width: 1200px; height: 824px; overflow: hidden; }
  .hero-photo {
    position: absolute; inset: 0;
    background: linear-gradient(180deg, var(--hero-top) 0%, var(--hero-mid) 55%, var(--hero-bottom) 100%);
  }
  .hero-content { position: absolute; inset: 0; color: var(--white); text-align: center; }
  .hero-title { position: absolute; top: 385px; left: 0; width: 1200px; font-size: 42px; font-weight: 700; line-height: 1; text-shadow: 0 1px 3px rgba(0,0,0,0.4); }
  .hero-lead { position: absolute; top: 435px; left: 128px; width: 944px; font-size: 14.2px; line-height: 21px; letter-spacing: -0.15px; }
  .hero-rule { position: absolute; left: 132px; width: 935px; height: 1px; background: rgba(255,255,255,0.22); }
  .hero-rule.first { top: 506px; }
  .hero-rule.second { top: 642px; }
  .margin-kicker { position: absolute; top: 529px; left: 0; width: 1200px; font-size: 14.5px; }
  .margin-title { position: absolute; top: 550px; left: 0; width: 1200px; font-size: 42px; font-weight: 700; line-height: 1.1; }
  .margin-sub { position: absolute; top: 598px; left: 0; width: 1200px; font-size: 14.5px; }

  .feature { position: absolute; top: 676px; text-align: left; }
  .feature-title { display: flex; align-items: center; gap: 8px; color: var(--brand-green); font-size: 21px; font-weight: 700; text-transform: uppercase; height: 26px; white-space: nowrap; }
  .feature-title svg { width: 26px; height: 26px; fill: var(--brand-green); flex: none; }
  .feature-text { margin-top: 10px; font-size: 10.4px; line-height: 16px; color: var(--body-muted); }
  .feature-button { display: inline-block; margin-top: 12px; width: 79px; height: 26px; line-height: 26px; text-align: center; background: var(--button-bg); color: var(--button-text); font-size: 10.5px; text-decoration: none; }
  .feature.advertise { left: 133px; width: 268px; }
  .feature.promote { left: 446px; width: 305px; }
  .feature.insurance { left: 795px; width: 275px; }

  .site-footer { position: absolute; top: 896px; left: 0; width: 1200px; height: 98px; background: var(--footer-bg); color: var(--footer-text); }
  .footer-links { position: absolute; left: 132px; top: 28px; font-size: 11.5px; display: flex; gap: 10px; }
  .footer-links a { color: var(--footer-text); text-decoration: none; }
  .copyright { position: absolute; left: 132px; top: 54px; font-size: 11.5px; word-spacing: 2px; }
  .social-list { position: absolute; left: 943px; top: 47px; display: flex; gap: 7px; list-style: none; }
  .social-list li { width: 26px; height: 26px; border-radius: 50%; background: var(--button-bg); }
</style>
</head>
<body>
  <div class="top-strip"></div>

  <header class="site-header">
    <div class="brand">
      <span class="brand-mark"></span>
      <span class="brand-name">DRIVEMARQ</span>
    </div>
    <nav class="main-nav">
      <a href="#" class="is-active">Home</a>
      <a href="#">Benefits</a>
      <a href="#">Vehicle Listings</a>
      <a href="#">Start Advertising Now</a>
      <a href="#">Contact</a>
    </nav>
  </header>

  <section class="hero">
    <div class="hero-photo" role="img" aria-label="Photo: red hatchback driving along a curving country road"></div>
    <div class="hero-content">
      <h1 class="hero-title">WE’VE GOT IT ARRANGED</h1>
      <p class="hero-lead">Drivemarq.com is an online platform which covers every single aspects from buying to selling of your vehicles. From engagement of a Servicing Agent till successfully handing over its ownership through a smarter and secure solutions.</p>
      <div class="hero-rule first"></div>
      <p class="margin-kicker">With Drivemarq.com platform</p>
      <h2 class="margin-title">THE MARGIN IS YOURS</h2>
      <p class="margin-sub">when you reaches out to potential vehicle enthusiasts directly.</p>
      <div class="hero-rule second"></div>

      <article class="feature advertise">
        <h3 class="feature-title">
          <svg viewBox="0 0 26 26" aria-hidden="true"><path d="M2 9h5l12-6v20L7 17H6l2 6H5l-2-6H2z"/><rect x="21" y="11" width="4" height="4"/></svg>
          Advertise Now
        </h3>
        <p class="feature-text">Upload images and vehicle details right after creating an account which is absolutely hassle &amp; cost free.</p>
        <a href="#" class="feature-button">Learn more</a>
      </article>

      <article class="feature promote">
        <h3 class="feature-title">
          <svg viewBox="0 0 26 26" aria-hidden="true"><path d="M9 4h8v3h7v7H2V7h7zm2 2v1h4V6z"/><path d="M2 15h9v2h4v-2h9v8H2z"/></svg>
          Promote Your Business
        </h3>
        <p class="feature-text">Leverage our busy online traffic which makes us an excellent business platform for limitless exposure.</p>
        <a href="#" class="feature-button">Learn more</a>
      </article>

      <article class="feature insurance">
        <h3 class="feature-title">
          <svg viewBox="0 0 26 26" aria-hidden="true"><path fill-rule="evenodd" d="M13 1a12 12 0 1 1 0 24 12 12 0 0 1 0-24zm0 6a6 6 0 1 0 0 12 6 6 0 0 0 0-12zm0 3a3 3 0 1 1 0 6 3 3 0 0 1 0-6z"/></svg>
          Online Insurance
        </h3>
        <p class="feature-text">Fill up your details on one form, we will provide several quotation to suits your requirement.</p>
        <a href="#" class="feature-button">Learn more</a>
      </article>
    </div>
  </section>

  <footer class="site-footer">
    <nav class="footer-links">
      <a href="#">Home</a><span>|</span>
      <a href="#">Benefits</a><span>|</span>
      <a href="#">Vehicle Listings</a><span>|</span>
      <a href="#">Start advertising Now</a><span>|</span>
      <a href="#">Contact</a>
    </nav>
    <p class="copyright">Copyright © 2016 Drivemarq. All rights reserved.</p>
    <ul class="social-list" aria-label="Social links">
      <li></li><li></li><li></li><li></li>
    </ul>
  </footer>
</body>
</html>
```